Skin cancer clinic services trifold brochure

Need trifold brochure listing skin cancer services our clinic provides, staff information, location and brief about skin cancer with colours similar to our web site www.Lumorava.clinic. I will provide more information regarding services and staff but want this colourful and standout as it will be given to other referring doctors or patients

Target Market(s)

Age 40 to 80 years

Industry/Entity Type

Medical

Font styles to use
Serif

Colors

Designer to choose colors to be used in the design.

Requirements
Must have
• Logo, services, contact info, beach or sun look and colours similar to web site or logo

```html
<!DOCTYPE html>
<html lang="en">
<head>
<meta charset="utf-8">
<title>Lumorava Skin Cancer Clinic – Trifold Brochure</title>
<link href="https://fonts.googleapis.com/css2?family=Montserrat:wght@300;400;600;700&display=swap" rel="stylesheet">
<style>
:root{
  --orange:#f0912a;
  --orange-deep:#e07a10;
  --orange-light:#f5a540;
  --ink:#3a3a3a;
  --muted:#5a5a5a;
  --paper:#ffffff;
  --backdrop:#4a4a4a;
}
*{box-sizing:border-box;margin:0;padding:0}
html,body{width:1200px;height:800px;overflow:hidden;background:var(--backdrop)}
body{font-family:'Montserrat',sans-serif;color:var(--ink)}
.brochure{display:flex;width:1200px;height:800px}
.panel{width:400px;height:800px;position:relative;overflow:hidden}
.panel-staff,.panel-treatments{background:var(--paper)}
.panel-services{background:linear-gradient(160deg,var(--orange-light) 0%,var(--orange) 45%,var(--orange-deep) 100%);color:#fff}
.panel-title{font-weight:300;font-size:30px;line-height:1.05;text-transform:uppercase;letter-spacing:.5px;border-left:3px solid var(--orange);padding-left:12px}
.panel-title strong{font-weight:700;color:var(--orange)}
.panel-services .panel-title{border-left-color:#fff}
.panel-services .panel-title strong{color:#fff}

/* staff */
.panel-staff{padding:60px 44px 0}
.staff-intro,.staff-outro{font-size:12px;line-height:1.5;margin-top:18px;color:var(--muted)}
.staff-list{list-style:none;margin-top:14px}
.staff-member{margin-bottom:12px}
.staff-name{font-size:19px;font-weight:700;color:var(--orange)}
.staff-quals{font-size:11.5px;color:var(--muted);line-height:1.35}
.beach-photo{position:absolute;left:0;bottom:0;width:400px;height:200px}
.fact-badge{position:absolute;right:28px;bottom:70px;width:130px;height:130px;border-radius:50%;background:var(--orange);color:#fff;text-align:center;display:flex;flex-direction:column;align-items:center;justify-content:center;padding:0 14px}
.fact-badge-label{background:#1e1e1e;font-weight:700;font-size:11px;padding:3px 8px;margin-bottom:6px;letter-spacing:.5px}
.fact-badge-text{font-size:10.5px;font-weight:600;line-height:1.3}

/* services */
.panel-services{padding:60px 40px 0}
.service-list{list-style:none;margin-top:24px}
.service-item{font-size:11px;line-height:1.45;margin-bottom:11px;color:#fff;opacity:.95}
.service-item b{font-weight:700}

/* treatments */
.panel-treatments{padding:60px 40px 0}
.treatment-list{list-style:none;margin-top:22px}
.treatment-item{font-size:11px;line-height:1.45;margin-bottom:11px;color:var(--muted)}
.treatment-item b{color:var(--orange);font-weight:600}
.treatment-item a{color:var(--orange);text-decoration:none}
.booking{margin-top:18px;border:1.5px solid var(--orange);position:relative}
.booking-label{background:var(--orange);color:#fff;font-size:15px;text-transform:uppercase;padding:6px 14px;letter-spacing:.5px}
.booking-phone{display:flex;align-items:center;gap:12px;padding:8px 14px;font-size:30px;font-weight:700;color:var(--orange)}
.booking-phone svg{width:26px;height:26px;flex:none}
</style>
</head>
<body>
<main class="brochure">

  <section class="panel panel-staff">
    <h2 class="panel-title">Our <strong>Staff</strong></h2>
    <p class="staff-intro">At Lumorava Skin Cancer Clinic, our highly qualified administrative staff, nurses and doctors are an integral part of the team ensuring excellent clinical care is provided to our patients. We currently have 5 experienced local doctors:</p>
    <ul class="staff-list">
      <li class="staff-member"><div class="staff-name">Dr. Maren Calloway</div><div class="staff-quals">Bmed, FRACGP, Diploma Skin Cancer Medicine/Surgery, Diploma Aesthetic Medicine</div></li>
      <li class="staff-member"><div class="staff-name">Dr. Tessa Quillan</div><div class="staff-quals">Bmed, FRACGP, Diploma Skin Cancer Medicine/Surgery</div></li>
      <li class="staff-member"><div class="staff-name">Dr. Helena Marchetti</div><div class="staff-quals">MBBS, FRACGP</div></li>
      <li class="staff-member"><div class="staff-name">Dr. Owen Hartley</div><div class="staff-quals">MBBS (Syd), Dip Law</div></li>
      <li class="staff-member"><div class="staff-name">Dr. Rosa Delaney</div><div class="staff-quals">MBBS (Hons), FRACGP, Cert. Skin Cancer Medicine</div></li>
    </ul>
    <p class="staff-outro">Early detection of skin cancers is vital for the best outcome. Lumorava has invested in technology and research to provide the latest diagnostic services and treatments to meet the needs of our patients.</p>

    <svg class="beach-photo" viewBox="0 0 400 200" role="img" aria-label="Photo of a child running through shallow sea water at the beach">
      <defs>
        <linearGradient id="beachTone" x1="0" y1="0" x2="0" y2="1">
          <stop offset="0" stop-color="#cfe6ef"/>
          <stop offset=".55" stop-color="#4fa3c4"/>
          <stop offset="1" stop-color="#2f7fa3"/>
        </linearGradient>
      </defs>
      <path d="M0 40 Q160 10 400 30 L400 200 L0 200 Z" fill="url(#beachTone)"/>
      <path d="M0 40 Q160 10 400 30" fill="none" stroke="var(--orange)" stroke-width="2"/>
    </svg>
    <div class="fact-badge">
      <span class="fact-badge-label">DID YOU KNOW?</span>
      <span class="fact-badge-text">Skin cancer accounts for 80% of all newly diagnosed cancers?</span>
    </div>
  </section>

  <section class="panel panel-services">
    <h2 class="panel-title">Professional<br><strong>Skin Services</strong></h2>
    <ul class="service-list">
      <li class="service-item"><b>Advanced Skin Cancer Detection</b> with detailed full body skin checks using dermoscopy and technology to minimise unnecessary excisions.</li>
      <li class="service-item"><b>Individual Mole mapping and full body photography</b> utilising intelligent skin analytics with SkinTrace, an AI-powered platform for documenting and diagnosing skin cancers that tracks changes over time.</li>
      <li class="service-item"><b>DermaView Skin Imaging System</b> which captures high quality images using proven technology, revealing detail up to 2mm beneath the skin's surface.</li>
      <li class="service-item"><b>Purpose Built Skin Cancer Facility</b> providing surgical treatments in 2 dedicated fully equipped theatres and treatment room staffed by skilled nurses.</li>
      <li class="service-item"><b>Large referral basis</b> for our patients that may require extensive therapy, including radiotherapy and Mohs surgery for sensitive areas.</li>
      <li class="service-item"><b>Priority Spot Checks</b> – appointments are set aside every day for urgent suspicious lesions, whether for an existing or new patient.</li>
      <li class="service-item"><b>GP Team Approach</b> – Lumorava believes an integrated team approach to a patient's skin cancer care is important, and results are shared with their GP.</li>
      <li class="service-item"><b>Pain minimisation Techniques</b> – topical numbing creams and ChillPoint numbing agents, and theatres with calming nature scenes to ensure our patients are comfortable.</li>
    </ul>
  </section>

  <section class="panel panel-treatments">
    <h2 class="panel-title">Specialised<br><strong>Treatments</strong></h2>
    <ul class="treatment-list">
      <li class="treatment-item"><b>Surgical Procedures</b> – Our Doctors are proficient in surgical procedures from simple diagnostic biopsies to advanced grafts and flap repair, all under local anaesthetic.</li>
      <li class="treatment-item"><b>RadioKnife Radiofrequency procedures</b> – a high frequency radiosurgical device allowing our Doctors to remove benign lesions, moles and skin tags with minimal thermal damage and faster recovery.</li>
      <li class="treatment-item"><b>Margin Controlled Surgery</b> (also known as Slow Mohs or Delayed Closure) – the wound is not closed until histological clearance is known, minimising the need for larger excisions.</li>
      <li class="treatment-item"><b>Non-surgical treatments and preventative therapy options</b> – Our goal is to prevent and treat skin cancer in the least invasive way, including Vitamin B3 and topical therapies.</li>
      <li class="treatment-item"><b>Cosmetic Services</b> – Lumorava approaches our skin cancer patients holistically and can offer advice on troublesome bumps and pigmentation. Please see our web site at <a href="#">www.Lumorava.clinic</a> for more information.</li>
    </ul>
    <div class="booking">
      <div class="booking-label">Book an appointment</div>
      <div class="booking-phone">
        <svg viewBox="0 0 24 24" aria-hidden="true"><circle cx="12" cy="12" r="11" fill="none" stroke="#333" stroke-width="2"/><path d="M8 6.5l2 2.2-1.2 1.6a8 8 0 0 0 4.9 4.9l1.6-1.2 2.2 2-1.4 1.7c-4.6-.6-8.6-4.6-9.2-9.2z" fill="#333"/></svg>
        <span>1300 58 7714</span>
      </div>
    </div>
  </section>

</main>
</body>
</html>
```